Velter Labs - Mushroom Supplement Packaging

Our brand is called Velter Labs. I've added a couple different logos that you can use. We are creating a line up of Mushroom Supplement products. I will add the entire line-up of products here. I've added examples of other products and packaging shape types I can purchase. Give me different options for packaging that is minimalist and clean for this brand that makes it look really well made and clean and make people want to buy.

Product 1 Lions Mane 1g
Product 2 Cordyceps 1g
Product 3 Chaga 1g
Product 4 Turkey Tail 1g
Product 5 Reishi 1g
Product 6 Maitake 1g
Product 7 Shiitake 1g

Product 8 (Mix) Lions Mane 143mg
Cordyceps 143mg
Chaga 143mg
Turkey Tail 143mg
Reishi 143mg
Maitake 143mg
Shiitake 143mg

```html
<!DOCTYPE html>
<html lang="en">
<head>
<meta charset="UTF-8">
<title>Velter Labs – Lions Mane Label</title>
<link href="https://fonts.googleapis.com/css2?family=Outfit:wght@400;500;700&display=swap" rel="stylesheet">
<style>
  :root {
    --backdrop: #e9e9ea;
    --label-dark: #1b1b1c;
    --label-mid: #2a2a2b;
    --gold: #e6b94a;
    --gold-deep: #d9a93a;
    --white: #f2f2f2;
    --band-grey: #b9b9bb;
    --band-text: #2a2a2a;
    --line-art: #6a6a6c;
  }
  * { margin: 0; padding: 0; box-sizing: border-box; }
  html, body {
    width: 1200px; height: 1200px; overflow: hidden;
    background: var(--backdrop);
    font-family: 'Outfit', sans-serif;
  }
  .label {
    position: absolute;
    left: 200px; top: 160px;
    width: 800px; height: 880px;
    background: linear-gradient(90deg, var(--label-dark) 0%, var(--label-mid) 45%, var(--label-dark) 100%);
    color: var(--white);
  }
  .brand {
    position: absolute;
    left: 110px; top: 150px;
    font-size: 58px; font-weight: 500;
    letter-spacing: 1px;
    color: var(--white);
    line-height: 1;
  }
  .product-name {
    position: absolute;
    left: 98px; top: 350px;
    font-size: 108px; font-weight: 700;
    color: var(--gold);
    letter-spacing: -1px;
    line-height: 1;
  }
  .type-band {
    position: absolute;
    left: 100px; top: 472px;
    width: 520px; height: 46px;
    background: linear-gradient(90deg, var(--band-grey), #d4d4d6);
    clip-path: polygon(0 0, 100% 0, 96% 100%, 0 100%);
    color: var(--band-text);
    font-size: 30px; font-weight: 700;
    line-height: 46px;
    padding-left: 12px;
    letter-spacing: -0.3px;
  }
  .benefits {
    position: absolute;
    left: 110px; top: 590px;
    font-size: 31px; font-weight: 400;
    line-height: 42px;
    color: var(--white);
  }
  .illustration {
    position: absolute;
    left: 510px; top: 545px;
    width: 265px; height: 295px;
    background: radial-gradient(ellipse at 50% 40%, #3a3a3c 0%, #262627 70%, transparent 100%);
    border-radius: 8px;
  }
  .count {
    position: absolute;
    left: 110px; top: 760px;
    display: flex; align-items: center; gap: 12px;
  }
  .count-text { line-height: 1; }
  .count-main {
    font-size: 34px; font-weight: 700; color: var(--gold);
  }
  .count-sub {
    font-size: 20px; font-weight: 500; color: var(--white);
    margin-top: 4px;
  }
  .gold-rule {
    position: absolute;
    left: 0; top: 835px;
    width: 100%; height: 3px;
    background: var(--gold-deep);
  }
</style>
</head>
<body>
  <section class="label">
    <div class="brand">Velter Labs</div>

    <h1 class="product-name">LIONS MANE</h1>
    <div class="type-band">MUSHROOM EXTRACT CAPSULES</div>

    <p class="benefits">Energy Support &amp; Immune<br>Balancing Properties</p>

    <div class="illustration" role="img" aria-label="Line drawing of a cluster of mushrooms"></div>

    <div class="count">
      <svg class="capsule-icon" width="56" height="48" viewBox="0 0 56 48" fill="none" stroke="#f2f2f2" stroke-width="2.5">
        <rect x="2" y="24" width="36" height="18" rx="9"/>
        <line x1="20" y1="24" x2="20" y2="42"/>
        <rect x="26" y="4" width="16" height="30" rx="8" transform="rotate(40 34 19)"/>
      </svg>
      <div class="count-text">
        <div class="count-main">60 CAPSULES</div>
        <div class="count-sub">DIETARY SUPPLEMENT</div>
      </div>
    </div>

    <div class="gold-rule"></div>
  </section>
</body>
</html>
```